Coporate Brochure

I want to create a 4-6 page brochure that presents our company , products and services to our clients. We want to focus on Products , service & repair

website is www.kvt-almsford.com
line card also downloadable from website as well.

Target Market(s)

Industrial Plants and Water treatment plants

Industry/Entity Type

Industrial engineering

Requirements
Must have
• Stock images of pumps, motors, blowers and valves
Nice to have
• Nice stock photos

```html
<!DOCTYPE html>
<html lang="en">
<head>
<meta charset="utf-8">
<title>KVT Brochure</title>
<link href="https://fonts.googleapis.com/css2?family=Montserrat:wght@400;500;600;700;800&family=Russo+One&display=swap" rel="stylesheet">
<style>
:root{
  --blue:#1f5fbf;
  --blue-dark:#163f8a;
  --ink:#1d1d1f;
  --band:#232325;
  --text:#3a3a3c;
  --muted:#6b6b70;
  --paper:#ffffff;
  --stage:#ececee;
  --steel-a:#d9dde2;
  --steel-b:#7d8590;
}
*{margin:0;padding:0;box-sizing:border-box}
html,body{width:1200px;height:3277px;overflow:hidden}
body{background:var(--stage);font-family:"Montserrat",sans-serif;color:var(--text);position:relative}
.spread{position:absolute;left:30px;width:1140px;height:740px;background:var(--paper);box-shadow:0 18px 40px rgba(0,0,0,.18);overflow:hidden}
.spread--cover{top:838px}
.spread--inner{top:1698px}
.spread svg.art{position:absolute;left:0;top:0;width:1140px;height:740px}
.abs{position:absolute}
.brand{font-family:"Montserrat",sans-serif;font-weight:800;color:var(--blue);font-size:40px;letter-spacing:2px}
.about-band{left:0;top:184px;width:640px;height:221px;background:var(--band)}
.about-title{left:44px;top:238px;font-size:31px;color:#fff;font-weight:400;letter-spacing:1px}
.about-title span{color:var(--blue);}
.about-title b{font-weight:800}
.about-copy{left:44px;top:295px;width:520px;font-size:10.5px;line-height:1.45;color:#e6e6e8}
.contact-title{left:44px;top:498px;font-size:14px;font-weight:700;color:var(--ink)}
.contact-title span{color:var(--blue)}
.contact-list{left:44px;top:540px;list-style:none;font-size:10.5px;line-height:1.4;color:var(--ink)}
.contact-list li{display:flex;gap:14px;margin-bottom:9px;align-items:flex-start}
.contact-list svg{width:11px;height:11px;flex:none;margin-top:2px}
.contact-divider{left:290px;top:528px;width:1px;height:98px;background:#9a9aa0}
.contact-web{left:350px;top:540px}
.headline{left:580px;top:555px;width:560px;text-align:center}
.headline h1{font-family:"Russo One",sans-serif;font-weight:400;font-size:42px;color:var(--ink);letter-spacing:2px;line-height:1}
.headline h2{font-family:"Russo One",sans-serif;font-weight:400;font-size:24px;color:var(--blue);letter-spacing:1.5px;margin-top:6px}
.headline p{font-size:10.5px;font-weight:700;color:var(--ink);margin-top:14px;line-height:1.35}
.logo-badge{left:805px;top:440px;width:120px;text-align:center;font-size:32px}
.section-title{font-weight:800;color:var(--blue);font-size:15px;letter-spacing:1px;text-transform:uppercase;display:flex;align-items:center;gap:10px;line-height:1.15}
.section-title::after{content:"";flex:1;border-top:2px dotted #8a8a90;margin-top:6px}
.products-title{left:28px;top:185px;font-size:19px;font-weight:800;color:var(--ink);letter-spacing:1px}
.products-title span{font-weight:700}
.thumb{border-radius:2px}
.blurb{font-size:8.6px;line-height:1.4;color:var(--text)}
.bullets{display:grid;list-style:none;font-size:7.6px;font-weight:600;color:var(--ink);text-transform:uppercase;row-gap:12px;column-gap:14px}
.bullets li{position:relative;padding-left:16px;line-height:1.2}
.bullets li::before{content:"";position:absolute;left:0;top:2px;width:5px;height:5px;border-radius:50%;background:var(--blue)}
.bullets--mixed{text-transform:none}
</style>
</head>
<body>

<!-- Outside spread: about + cover -->
<section class="spread spread--cover">
  <div class="abs about-band"></div>
  <div class="abs brand" style="left:44px;top:102px">KVT</div>
  <h2 class="abs about-title"><span>ABOUT</span> <b>KVT</b></h2>
  <p class="abs about-copy">Kinetic Valve Technologies Inc. offer sales &amp; service of equipment including pumps, mixers, valves, blowers, filtration &amp; bulk process solutions to the industrial, municipal &amp; fire sprinkler markets</p>

  <h3 class="abs contact-title"><span>CONTACT</span> DETAILS</h3>
  <ul class="abs contact-list">
    <li><svg viewBox="0 0 12 12"><path d="M2 1l2 0 1 3-1.5 1a6 6 0 0 0 3 3L7.5 6.5l3 1 0 2a1.5 1.5 0 0 1-1.5 1.5A8.5 8.5 0 0 1 .5 2.5 1.5 1.5 0 0 1 2 1z" fill="#1d1d1f"/></svg>(555)310-4420</li>
    <li><svg viewBox="0 0 12 12"><rect x="1" y="3" width="10" height="7" fill="#1d1d1f"/><rect x="3" y="1" width="6" height="3" fill="#1d1d1f"/></svg>(555)310-4481</li>
    <li><svg viewBox="0 0 12 12"><path d="M6 .5a4 4 0 0 0-4 4c0 3 4 7 4 7s4-4 4-7a4 4 0 0 0-4-4zm0 5.5a1.5 1.5 0 1 1 0-3 1.5 1.5 0 0 1 0 3z" fill="#1d1d1f"/></svg>420 Mill Creek Rd.<br>Almsford VA 20145</li>
  </ul>
  <div class="abs contact-divider"></div>
  <ul class="abs contact-list contact-web">
    <li><svg viewBox="0 0 12 12"><rect x="1" y="2.5" width="10" height="7" fill="#1d1d1f"/><path d="M1 2.5l5 4 5-4" stroke="#fff" fill="none"/></svg>sales@kvt-almsford.com</li>
    <li><svg viewBox="0 0 12 12"><circle cx="6" cy="6" r="5" fill="none" stroke="#1d1d1f" stroke-width="1.4"/><path d="M1 6h10M6 1c2.5 3 2.5 7 0 10M6 1c-2.5 3-2.5 7 0 10" stroke="#1d1d1f" fill="none"/></svg>kvt-almsford.com</li>
  </ul>

  <svg class="art" viewBox="0 0 1140 740" aria-hidden="false">
    <defs>
      <linearGradient id="steel" x1="0" y1="0" x2="1" y2="1">
        <stop offset="0" stop-color="var(--steel-a)"/><stop offset=".55" stop-color="var(--steel-b)"/><stop offset="1" stop-color="#4f5761"/>
      </linearGradient>
      <clipPath id="coverClip"><rect x="0" y="0" width="1140" height="740"/></clipPath>
    </defs>
    <g clip-path="url(#coverClip)">
      <circle cx="898" cy="182" r="322" fill="var(--blue)"/>
      <circle cx="908" cy="165" r="306" fill="#fff"/>
      <circle cx="910" cy="160" r="300" fill="url(#steel)" role="img" aria-label="Photo of stainless process piping with blue flow meters in an industrial plant"/>
      <rect x="0" y="0" width="1140" height="0" fill="none"/>
    </g>
    <circle cx="865" cy="465" r="82" fill="#fff"/>
  </svg>
  <div class="abs brand logo-badge">KVT</div>

  <div class="abs headline">
    <h1>LIQUID &amp; DRY</h1>
    <h2>PROCESS EQUIPMENT</h2>
    <p>WE APPRECIATE EVERY OPPORTUNITY PRESENTED AND LOOK FORWARD<br>TO BECOMING A VALUABLE RESOURCE TO YOUR BUSINESS.</p>
  </div>
</section>

<!-- Inside spread: products -->
<section class="spread spread--inner">
  <svg class="art" viewBox="0 0 1140 740">
    <defs>
      <linearGradient id="plant" x1="0" y1="0" x2="1" y2="0">
        <stop offset="0" stop-color="#8a7f72"/><stop offset=".5" stop-color="#5d5a55"/><stop offset="1" stop-color="#a39a8e"/>
      </linearGradient>
      <linearGradient id="tanks" x1="0" y1="0" x2="1" y2="1">
        <stop offset="0" stop-color="#e3e8ec"/><stop offset="1" stop-color="#8c979f"/>
      </linearGradient>
      <clipPath id="innerClip"><rect x="0" y="0" width="1140" height="740"/></clipPath>
    </defs>
    <g clip-path="url(#innerClip)">
      <rect x="0" y="0" width="570" height="165" fill="url(#plant)" role="img" aria-label="Photo of a pump room with pipework and valves"/>
      <circle cx="95" cy="25" r="175" fill="var(--blue)"/>
      <circle cx="85" cy="15" r="168" fill="#fff"/>
      <circle cx="1075" cy="660" r="120" fill="var(--blue)"/>
      <circle cx="1085" cy="650" r="112" fill="#fff"/>
      <circle cx="1088" cy="648" r="106" fill="url(#tanks)" role="img" aria-label="Photo of stainless chemical skid tanks"/>
    </g>
  </svg>
  <div class="abs brand" style="left:20px;top:62px;font-size:34px">KVT</div>

  <!-- Left page -->
  <h2 class="abs products-title">OUR PRODUCTS</h2>

  <h3 class="abs section-title" style="left:30px;top:225px;width:510px">Pumps &amp; Systems</h3>
  <div class="abs thumb" style="left:30px;top:256px;width:125px;height:86px;background:linear-gradient(135deg,#4f7fc4,#1e3d6e)" role="img" aria-label="Photo of blue centrifugal pumps"></div>
  <p class="abs blurb" style="left:172px;top:262px;width:365px">Kinetic Valve Technologies (KVT) has regional representatives throughout Virginia, Maryland &amp; North Carolina to provide unmatched technical sales &amp; service support for all your pump needs. For over 30 years, KVT has been committed to providing a selection of premium, energy efficient centrifugal &amp; positive displacement pumps to satisfy virtually any pumping application. An inventory of quality commercial pumps and parts for all brands, coupled with our high-quality service, makes KVT your first choice for industrial, municipal, and commercial pumping needs.</p>
  <ul class="abs bullets" style="left:30px;top:364px;width:520px;grid-template-columns:repeat(5,1fr)">
    <li>Vertical Pumps</li><li>ANSI</li><li>End Suction</li><li>Fiberglass Pumps</li><li>Progressive Cavity</li>
    <li>Split Case</li><li>Non Clog</li><li>High Temperature</li><li>Magnetic Drive</li><li>Metering/Dosing</li>
    <li>Rotary Lobe</li><li>Booster</li><li>Commercial Water</li><li>Self Priming</li><li>Booster Skids</li>
    <li>Peristaltic Lobe</li><li>Grinder</li><li>Submersible</li><li>AODD</li><li>Dosing Systems</li>
  </ul>

  <h3 class="abs section-title" style="left:30px;top:484px;width:510px">Blowers &amp; Packages</h3>
  <div class="abs thumb" style="left:30px;top:512px;width:125px;height:86px;background:linear-gradient(135deg,#3f6aa8,#2a3240)" role="img" aria-label="Photo of a blower package unit"></div>
  <p class="abs blurb" style="left:172px;top:520px;width:365px">Kinetic Valve Technologies (KVT) is a leading supplier of New &amp; Re-manufactured Positive Displacement Blowers. We provide only the highest quality Blowers and Blower Packages. For over 30 years we have developed a reputation as trusted partner to our customers for application design, custom blower packaging &amp; after sale service. Our capabilities include:</p>
  <ul class="abs bullets bullets--mixed" style="left:30px;top:622px;width:520px;grid-template-columns:1.1fr 1.1fr 1fr 1.2fr">
    <li>Lobe Blowers</li><li>Sound Enclosures</li><li>Belts &amp; Sheaves</li><li>Economy Packages</li>
    <li>Roots Type Blowers</li><li>Industrial Fans</li><li>Silencers</li><li>Standard Packages</li>
    <li>Lubrication</li><li>Relief Valves</li><li>Rebuilds</li><li>Filters</li>
  </ul>

  <!-- Right page -->
  <h3 class="abs section-title" style="left:600px;top:40px;width:510px">Dry Material<br>Handling</h3>
  <div class="abs thumb" style="left:600px;top:92px;width:125px;height:86px;background:linear-gradient(135deg,#b9c6d2,#5a6b7c)" role="img" aria-label="Photo of a worker at a bulk material conveyor line"></div>
  <p class="abs blurb" style="left:742px;top:104px;width:360px">Kinetic Valve Technologies (KVT) is a leading supplier of New &amp; Re-manufactured Positive Displacement Blowers. We provide only the highest quality Blowers and Blower Packages. For over 30 years we have developed a reputation as trusted partner to our customers for application design, custom blower packaging &amp; after sale service. Our capabilities include:</p>
  <ul class="abs bullets" style="left:600px;top:204px;width:520px;grid-template-columns:repeat(4,1fr)">
    <li>Belt Conveyors</li><li>Screw Conveyors</li><li>Rotary Valves</li><li>Palletizers</li>
    <li>Bagging Machines</li><li>Pneumatic Conveyors</li><li>Weighing Systems</li><li>Bag Dump Stations</li>
    <li>Tubular Cable Conveyors</li><li>Bulk Bag Fillers</li><li>Blower Package</li><li>Full Systems</li>
  </ul>

  <h3 class="abs section-title" style="left:600px;top:303px;width:510px">Fire Protection</h3>
  <div class="abs thumb" style="left:600px;top:330px;width:125px;height:86px;background:linear-gradient(135deg,#e04a3a,#8c2a22)" role="img" aria-label="Photo of a red fire pump system"></div>
  <p class="abs blurb" style="left:742px;top:340px;width:360px">Kinetic Valve Technologies (KVT) represents Ridgeline fire pumps &amp; systems throughout the state of Virginia. With over 90 years of progressive Ridgeline designing, engineering and manufacturing, Ridgeline pumps are proven with thousands of pump unit installations around the world. With proven success and an outstanding reputation Ridgeline Pumps is recognized as one of the leaders in this industry.</p>
  <p class="abs blurb" style="left:600px;top:430px;width:510px">Ridgeline Pumps designs tough, versatile products to meet your pumping needs. The fire pump units, systems, and housed packaged systems offer variety, durability, standardized options and configurations true to their outstanding reputation. Thousands of Ridgeline Pump installations (UL, ULC, or FM approved) deliver superior fire protection to facilities worldwide. Products are designed from a broad selection of pumps, drives, controls, baseplates and accessories.</p>
  <ul class="abs bullets bullets--mixed" style="left:600px;top:500px;width:510px;grid-template-columns:1fr 1.1fr 1.3fr 1fr">
    <li>Fire Pumps</li><li>Jockey Pumps</li><li>Electric Motors</li><li>Diesel Engines</li>
    <li>Controllers</li><li>Skid Packages</li><li>Fully Enclosed Packages</li><li>Service &amp; Repair</li>
  </ul>

  <h3 class="abs section-title" style="left:600px;top:575px;width:360px">Booster, Cooling<br>&amp; Chemical Skids</h3>
  <div class="abs thumb" style="left:600px;top:625px;width:125px;height:86px;background:linear-gradient(135deg,#4a72c0,#22304a)" role="img" aria-label="Photo of a blue booster pump skid"></div>
  <p class="abs blurb" style="left:742px;top:630px;width:210px">Kinetic Valve Technologies (KVT) offers pre-packaged pumping systems that are tailored to your specific application or need. From water and wastewater, to pulp and paper and chemical, packaged pump skids will keep your product moving with accuracy and efficiency.</p>
</section>

</body>
</html>
```